Student Card

we are college and require a student card which we issue on enlroment to students, just like a univeristy.

Baisic information need to be placed is:
Student photo
student ID
date of birth
exp date

our college contact details on the rear
its a tool for branding so its important the theme is in line with our colours and logo, please view our website www.harlowmereinstitute.net.au

Industry/Entity Type

College

```html
<!DOCTYPE html>
<html lang="en">
<head>
<meta charset="utf-8">
<title>Harlowmere Institute – Student Identity Card</title>
<link rel="stylesheet" href="https://fonts.googleapis.com/css2?family=Fira+Sans:wght@300;400;500;600&display=swap">
<style>
  :root {
    --canvas-bg: #eef1f2;
    --card-front: #7ff5e1;
    --card-back: #c6fbf0;
    --brand-blue: #2f5cf2;
    --ink: #141414;
    --photo-fill: #e6eceb;
    --photo-border: #1a1a1a;
    --emboss-light: rgba(255, 255, 255, 0.55);
    --emboss-dark: rgba(120, 200, 190, 0.35);
  }
  * { box-sizing: border-box; margin: 0; padding: 0; }
  html, body {
    width: 1200px; height: 1000px; overflow: hidden;
    background: var(--canvas-bg);
    font-family: "Fira Sans", sans-serif;
    color: var(--ink);
  }
  .sheet { position: relative; width: 1200px; height: 1000px; }

  .card {
    position: absolute; left: 220px;
    width: 760px; height: 470px;
    border-radius: 4px;
    box-shadow: 0 2px 8px rgba(0,0,0,0.12);
    overflow: hidden;
  }

  /* Rear side */
  .card--back { top: 18px; background: var(--card-back); text-align: center; padding-top: 38px; }
  .campus { margin-bottom: 26px; }
  .campus__heading { color: var(--brand-blue); font-weight: 600; font-size: 25px; line-height: 1.25; }
  .campus__org { font-weight: 500; font-size: 21px; line-height: 1.4; }
  .campus__line { font-size: 19px; line-height: 1.45; }
  .campus__label { color: var(--brand-blue); }

  /* Front side */
  .card--front { top: 512px; background: var(--card-front); }
  .front__college {
    position: absolute; left: 40px; top: 26px;
    color: var(--brand-blue); font-weight: 600; font-size: 42px; letter-spacing: 0.2px;
  }
  .front__title {
    position: absolute; left: 40px; top: 76px;
    font-weight: 400; font-size: 44px;
  }
  .front__brand {
    position: absolute; right: 30px; top: 34px;
    display: flex; align-items: center; gap: 6px;
    font-size: 11px; font-weight: 500; color: var(--ink);
  }
  .front__brand-dot { width: 18px; height: 18px; border-radius: 50%; background: var(--brand-blue); }
  .front__photo {
    position: absolute; left: 40px; top: 168px;
    width: 220px; height: 270px;
    background: var(--photo-fill);
    border: 3px dotted var(--photo-border);
  }
  .front__emboss {
    position: absolute; right: 20px; bottom: 0;
    width: 250px; height: 330px;
    border-radius: 40px 40px 0 0;
    background: linear-gradient(160deg, var(--emboss-light), var(--emboss-dark) 60%, transparent);
  }
  .front__details { position: absolute; left: 320px; top: 160px; }
  .field { margin-bottom: 10px; }
  .field__label { color: var(--brand-blue); font-size: 26px; font-weight: 400; line-height: 1.15; }
  .field__value { font-size: 28px; font-weight: 400; line-height: 1.15; letter-spacing: 0.5px; }
</style>
</head>
<body>
<main class="sheet">

  <section class="card card--back" aria-label="Card rear – contact details">
    <div class="campus">
      <p class="campus__heading">Head Office – Brisbane Campus</p>
      <p class="campus__org">Harlowmere Institute</p>
      <p class="campus__line">Level 2, 14 Carrow Lane, Eastfield, Queensland 4170 Australia</p>
      <p class="campus__line"><span class="campus__label">Tel:</span> +61 7 3000 4812 <span class="campus__label">Fax:</span> +61 7 3000 4813</p>
      <p class="campus__line"><span class="campus__label">Email:</span> info@harlowmereinstitute.net.au</p>
    </div>
    <div class="campus">
      <p class="campus__heading">City Campus</p>
      <p class="campus__org">Harlowmere Institute</p>
      <p class="campus__line">Level 1, 8 Marlow Road, Southbank, Queensland 4101 Australia</p>
      <p class="campus__line"><span class="campus__label">Tel:</span> +61 7 3000 4820 <span class="campus__label">Fax:</span> +61 7 3000 4821</p>
      <p class="campus__line"><span class="campus__label">Web:</span> www.harlowmereinstitute.net.au</p>
    </div>
  </section>

  <section class="card card--front" aria-label="Card front – student identity">
    <div class="front__emboss" role="img" aria-label="Faint embossed college mascot decoration"></div>
    <h1 class="front__college">Harlowmere Institute</h1>
    <h2 class="front__title">Student Identity Card</h2>
    <div class="front__brand"><span class="front__brand-dot"></span>Harlowmere Institute</div>
    <div class="front__photo" role="img" aria-label="Student photo area"></div>
    <dl class="front__details">
      <div class="field"><dt class="field__label">NAME</dt><dd class="field__value">A.N OTHER</dd></div>
      <div class="field"><dt class="field__label">STUDENT ID NUMBER</dt><dd class="field__value">123456789</dd></div>
      <div class="field"><dt class="field__label">DATE OF BIRTH</dt><dd class="field__value">01/01/1901</dd></div>
      <div class="field"><dt class="field__label">EXP DATE</dt><dd class="field__value">01/01/1901</dd></div>
    </dl>
  </section>

</main>
</body>
</html>
```